Business Card + Stationery Design for a Craft Beer Bar

Mr. Tolvek's is a taproom sport bar that contains in its menu beers from different places around the world. What we offer differently is the experience that you can get inside our location, ambient music with rock from the 80s to 90s, projection with the sports of the moment, board games and private events.

Target Market(s)

Young people, Mid and High Class

Industry/Entity Type

Business

Font styles to use
Serif
Sans Serif

Colors
fee18a

Requirements
Must have
• Name, Title, Contact Details, Website
Nice to have
• Mail Signature
Should not have
• n/a

```html
<!DOCTYPE html>
<html lang="en">
<head>
<meta charset="utf-8">
<title>Mr. Tolvek's Taproom – Stationery</title>
<link rel="stylesheet" href="https://fonts.googleapis.com/css2?family=Roboto:wght@400;500&display=swap">
<style>
  :root {
    --backdrop: #e3e3e3;
    --paper: #f7f7f7;
    --ink: #0b0b0b;
    --text: #555555;
    --body-text: #6a6a6a;
    --gold: #f4c14b;
    --faint: #ebebeb;
    --rule: #d4d4d4;
  }
  * { box-sizing: border-box; margin: 0; padding: 0; }
  html, body { width: 1200px; height: 546px; overflow: hidden; }
  body { background: var(--backdrop); font-family: "Roboto", Arial, sans-serif; color: var(--text); position: relative; }

  .piece { position: absolute; background: var(--paper); box-shadow: 0 1px 3px rgba(0,0,0,.18); overflow: hidden; }
  .piece--dark { background: var(--ink); }

  .footer-band { position: absolute; left: 0; right: 0; bottom: 0; height: 4px; display: flex; }
  .footer-band .band-dark { flex: 0 0 78%; background: var(--ink); }
  .footer-band .band-gold { flex: 1; background: var(--gold); }

  .brand { position: absolute; display: flex; flex-direction: column; align-items: center; }
  .brand-dot { border-radius: 50%; background: var(--ink); }
  .brand-name { font-family: "Roboto", Arial, sans-serif; font-weight: 500; color: var(--ink); line-height: 1.1; white-space: nowrap; }
  .piece--dark .brand-dot { background: #ffffff; }
  .piece--dark .brand-name { color: #ffffff; }

  .faint-mark { position: absolute; border-radius: 50%; background: var(--faint); }

  .contact { list-style: none; font-size: 5px; line-height: 6.4px; color: var(--text); }
  .contact li { display: flex; align-items: center; gap: 3px; }
  .contact .icon { width: 3.5px; height: 3.5px; border-radius: 1px; background: var(--gold); flex: none; }

  /* business card front */
  .card-front { left: 36px; top: 45px; width: 202px; height: 115px; }
  .card-front .brand { left: 10px; top: 34px; width: 82px; }
  .card-front .brand-dot { width: 20px; height: 20px; margin-bottom: 6px; }
  .card-front .brand-name { font-size: 11px; }
  .card-front .divider { position: absolute; left: 96px; top: 26px; width: 1px; height: 62px; background: var(--rule); }
  .card-front .details { position: absolute; left: 107px; top: 24px; }
  .holder-name { font-size: 7.5px; font-weight: 500; color: var(--gold); text-transform: uppercase; line-height: 8px; }
  .holder-title { font-size: 5px; font-weight: 500; color: var(--ink); text-transform: uppercase; margin-bottom: 4px; }
  .card-front .address { font-size: 5px; line-height: 6px; margin-bottom: 4px; }

  /* business card back */
  .card-back { left: 214px; top: 119px; width: 202px; height: 115px; }
  .card-back .brand { left: 0; right: 0; top: 30px; }
  .card-back .brand-dot { width: 24px; height: 24px; margin-bottom: 10px; }
  .card-back .brand-name { font-size: 13px; }

  /* envelope back */
  .envelope-back { left: 86px; top: 262px; width: 330px; height: 151px; }
  .envelope-back .flap { position: absolute; left: 0; right: 0; top: 0; height: 47px; background: var(--ink); border-radius: 0 0 16px 16px / 0 0 14px 14px; }
  .envelope-back .flap-dot { position: absolute; left: 158px; top: 13px; width: 14px; height: 14px; border-radius: 50%; background: #ffffff; }

  /* envelope front */
  .envelope-front { left: 41px; top: 350px; width: 332px; height: 152px; }
  .envelope-front .brand { left: 12px; top: 14px; width: 82px; }
  .envelope-front .brand-dot { width: 18px; height: 18px; margin-bottom: 6px; }
  .envelope-front .brand-name { font-size: 10px; }
  .envelope-front .address { position: absolute; left: 12px; top: 64px; width: 82px; text-align: center; font-size: 4.6px; line-height: 5.6px; color: var(--ink); }
  .envelope-front .faint-mark { left: 240px; top: 20px; width: 78px; height: 78px; }

  /* letterhead */
  .letterhead { left: 446px; top: 40px; width: 329px; height: 462px; }
  .letterhead .brand { left: 22px; top: 32px; width: 66px; }
  .letterhead .brand-dot { width: 18px; height: 18px; margin-bottom: 5px; }
  .letterhead .brand-name { font-size: 9px; }
  .letterhead .divider { position: absolute; left: 230px; top: 32px; width: 1px; height: 48px; background: var(--rule); }
  .letterhead .header-details { position: absolute; left: 237px; top: 31px; }
  .letterhead .address { font-size: 4.6px; line-height: 5.6px; margin-bottom: 3px; }
  .letterhead .contact { font-size: 4.6px; line-height: 5.8px; }
  .letterhead .faint-mark { left: 112px; top: 128px; width: 116px; height: 116px; }
  .letter-body { position: absolute; left: 28px; top: 130px; width: 276px; }
  .salutation { font-size: 9px; color: #444; margin-bottom: 14px; }
  .letter-body p { font-size: 4.8px; line-height: 7.2px; margin-bottom: 7px; color: var(--body-text); }
  .letter-body .closing { margin-top: 12px; margin-bottom: 8px; }
  .signature { width: 60px; height: 24px; background: #ededed; border-radius: 3px; }

  /* folder */
  .folder { left: 805px; top: 40px; width: 364px; height: 463px; }
  .folder .spine { position: absolute; top: 0; bottom: 0; width: 1px; background: #333; }
  .folder .spine--a { left: 7px; }
  .folder .spine--b { left: 17px; }
  .folder .brand { left: 10px; right: 0; top: 158px; }
  .folder .brand-dot { width: 50px; height: 50px; margin-bottom: 48px; }
  .folder .brand-name { font-size: 30px; }
</style>
</head>
<body>

  <section class="piece card-front" aria-label="Business card front">
    <div class="brand">
      <span class="brand-dot"></span>
      <span class="brand-name">Mr. Tolvek's</span>
    </div>
    <span class="divider"></span>
    <div class="details">
      <div class="holder-name">Dana Kerrow</div>
      <div class="holder-title">CEO/Founder</div>
      <div class="address">418 Copperfield Lane<br>Brookmere, Vermont 05461</div>
      <ul class="contact">
        <li><span class="icon"></span>614 220 7391</li>
        <li><span class="icon"></span>614 220 7392</li>
        <li><span class="icon"></span>614 220 7393</li>
        <li><span class="icon"></span>hello@tolvekstaproom.com</li>
        <li><span class="icon"></span>www.tolvekstaproom.com</li>
      </ul>
    </div>
    <div class="footer-band"><span class="band-dark"></span><span class="band-gold"></span></div>
  </section>

  <section class="piece piece--dark card-back" aria-label="Business card back">
    <div class="brand">
      <span class="brand-dot"></span>
      <span class="brand-name">Mr. Tolvek's</span>
    </div>
  </section>

  <section class="piece envelope-back" aria-label="Envelope back">
    <div class="flap"></div>
    <span class="flap-dot"></span>
  </section>

  <section class="piece envelope-front" aria-label="Envelope front">
    <div class="brand">
      <span class="brand-dot"></span>
      <span class="brand-name">Mr. Tolvek's</span>
    </div>
    <div class="address">418 Copperfield Lane<br>Brookmere, Vermont 05461</div>
    <span class="faint-mark"></span>
    <div class="footer-band"><span class="band-dark"></span><span class="band-gold"></span></div>
  </section>

  <section class="piece letterhead" aria-label="Letterhead">
    <div class="brand">
      <span class="brand-dot"></span>
      <span class="brand-name">Mr. Tolvek's</span>
    </div>
    <span class="divider"></span>
    <div class="header-details">
      <div class="address">418 Copperfield Lane<br>Brookmere, Vermont 05461</div>
      <ul class="contact">
        <li><span class="icon"></span>614 220 7391</li>
        <li><span class="icon"></span>614 220 7392</li>
        <li><span class="icon"></span>614 220 7393</li>
        <li><span class="icon"></span>hello@tolvekstaproom.com</li>
        <li><span class="icon"></span>www.tolvekstaproom.com</li>
      </ul>
    </div>
    <span class="faint-mark"></span>
    <div class="letter-body">
      <div class="salutation">Dear Ms. Kerrow,</div>
      <p>Thank you for joining us for the season opener at our taproom. This month our taps will pour new craft brews from six countries, from crisp pilsners to dark and roasty stouts, and the big screen will carry every major match of the week. Bring your friends, book a table early, and ask our staff about the private room for your next gathering or birthday party.</p>
      <p>Board game nights return every Thursday with a fresh shelf of classics and a few new favourites. The playlist stays loud with rock from the eighties and nineties, and our team will gladly pair a pint with any game you choose. Regulars can collect stamps on a card and trade a full card for a tasting flight of the house selection.</p>
      <p>We would be glad to host your company event or private celebration. Our crew can plan a menu around your guests, set the screens for any match or slideshow, and keep the glasses full from the first toast to the final whistle. Groups of twelve or more receive a welcome round on the house and a reserved corner near the stage, so everyone can hear the music and still talk.</p>
      <p>Please reply by the end of the month so we can hold your preferred date. If you have any questions about the menu, the schedule or the room layout, simply call or write to us and we will answer within a day.</p>
      <p class="closing">Sincerely,</p>
      <div class="signature" role="img" aria-label="Handwritten signature"></div>
    </div>
    <div class="footer-band"><span class="band-dark"></span><span class="band-gold"></span></div>
  </section>

  <section class="piece piece--dark folder" aria-label="Presentation folder">
    <span class="spine spine--a"></span>
    <span class="spine spine--b"></span>
    <div class="brand">
      <span class="brand-dot"></span>
      <span class="brand-name">Mr. Tolvek's</span>
    </div>
  </section>

</body>
</html>
```